Web Design Project

kestrel ridge works & services needs a new web design to go with its new logo design

we provide services such as instillation of fire sprinklers, fire hydrants , fire hose reels as well as fire extinguishers and fire blankets.

we can service these as well and also do the preventitave maintaince of these too.

we can do flow testing of sprinklers,hydrants & hosereels and test back flow prevention devices as well

old page is krws.com.au

```html
<!DOCTYPE html>
<html lang="en">
<head>
<meta charset="utf-8">
<title>Kestrel Ridge Works &amp; Services</title>
<link rel="stylesheet" href="https://fonts.googleapis.com/css2?family=Arimo:wght@400;700&family=Carlito&family=Open+Sans&display=swap">
<style>
:root{
  --amber:#fcbd49;
  --orange:#f7941d;
  --orange-light:#fbb040;
  --orange-dark:#c8700c;
  --red:#b3222b;
  --ink:#222;
  --grey:#555;
  --line:#c9c9c9;
  --white:#fff;
}
*{box-sizing:border-box;margin:0;padding:0}
html,body{width:978px;height:1200px;overflow:hidden;background:var(--white)}
body{position:relative;font-family:Arimo,Arial,sans-serif;color:var(--ink)}
.backdrop{position:absolute;left:0;top:0;width:978px;height:426px;background:var(--amber);box-shadow:0 2px 3px rgba(0,0,0,.25)}
.page{position:absolute;left:60px;top:0;width:844px;height:1200px;background:var(--white)}
.abs{position:absolute}
.brand{left:0;top:38px;width:844px;text-align:center;display:flex;justify-content:center;align-items:center;gap:10px;font-family:Carlito,sans-serif;font-size:24px;color:var(--red);font-weight:400}
.brand-mark{width:22px;height:22px;background:var(--red)}
.nav{left:0;top:147px;width:844px;height:60px;border-radius:0 0 10px 10px;background:var(--orange-dark);box-shadow:0 3px 3px rgba(0,0,0,.25)}
.nav ul{list-style:none;display:flex;height:50px}
.nav li{flex:1;height:50px;background:linear-gradient(var(--orange-light) 0 24%,var(--orange) 24%);color:var(--white);font-size:14px;text-align:center;padding-top:18px;border-left:3px solid var(--white)}
.nav li:first-child{border-left:0;background:linear-gradient(#f08a00 0 24%,var(--orange-dark) 24%)}
.nav-base{left:0;top:197px;width:844px;height:10px;background:var(--orange);border-radius:0 0 10px 10px}
.hero{left:0;top:218px;width:844px;height:279px;border-radius:10px 10px 0 0;background:linear-gradient(180deg,#b9b6ad 0%,#8f8a83 45%,#6f6660 100%)}
.pager{left:0;top:497px;width:844px;height:39px;border:1px solid var(--line);border-top:0;border-radius:0 0 10px 10px;display:flex;justify-content:center;align-items:center;gap:14px;font-size:20px}
.pager .on{width:24px;height:24px;border-radius:50%;background:#111;color:var(--white);display:flex;align-items:center;justify-content:center}
.card{border:1px solid var(--line);border-radius:10px;box-shadow:0 2px 3px rgba(0,0,0,.2);background:var(--white)}
.features{left:0;top:541px;width:552px;height:333px}
.feature h2{font-family:Carlito,sans-serif;font-weight:400;font-size:23px;text-align:center;width:290px}
.feature .photo{border-radius:10px;width:207px;height:106px}
.divider{left:296px;top:36px;width:1px;height:240px;background:var(--line)}
.more{background:#000;color:var(--white);font-family:Carlito,sans-serif;font-size:23px;width:72px;height:31px;text-align:center;line-height:31px}
.hotline{left:558px;top:541px;width:286px;height:153px;overflow:hidden}
.hotline h3{background:var(--red);color:var(--white);font-family:Carlito,sans-serif;font-weight:400;font-size:27px;line-height:30px;height:83px;padding:13px 8px 0 8px;text-align:right}
.hotline p{font-family:"Open Sans",sans-serif;font-size:40px;color:var(--grey);padding:4px 0 0 10px}
.contact{left:558px;top:719px;width:286px;height:154px;padding:6px 12px;font-size:12.5px;line-height:15px;color:#333}
.contact h3{font-family:Arimo,sans-serif;font-weight:400;font-size:31px;line-height:34px;color:#111;display:inline-block;border-bottom:2px solid #111;margin-bottom:8px}
.about{left:0;top:879px;width:844px;height:240px;padding:3px 10px;font-size:15.4px;line-height:19px;color:#333}
.about p{margin-bottom:18px}
.footer{left:0;top:1126px;width:844px;height:50px;border-bottom:4px solid var(--orange-dark);text-align:center;font-size:19px;padding-top:10px}
</style>
</head>
<body>
<div class="backdrop"></div>
<div class="page">
  <header class="brand abs"><span class="brand-mark"></span><span>Kestrel Ridge Works &amp; Services</span></header>
  <nav class="nav abs">
    <ul><li>Home</li><li>Service</li><li>Testing</li><li>Products</li><li>FAQ's</li><li>Contact</li><li>Service</li><li>Service</li></ul>
  </nav>
  <div class="hero abs" role="img" aria-label="Street scene with a red fire hydrant beside a paved footpath"></div>
  <div class="pager abs">
    <svg width="20" height="26" viewBox="0 0 20 26"><path d="M16 2 4 13l12 11" fill="none" stroke="#aaa" stroke-width="2"/></svg>
    <span class="on">1</span><span>2</span><span>3</span><span>4</span><span>5</span>
    <svg width="20" height="26" viewBox="0 0 20 26"><path d="M4 2l12 11L4 24" fill="none" stroke="#aaa" stroke-width="2"/></svg>
  </div>

  <section class="features card abs">
    <div class="feature abs" style="left:4px;top:24px">
      <h2>Use the Right Extinguisher</h2>
      <div class="photo abs" style="left:28px;top:30px;background:linear-gradient(135deg,#9aa5a4,#6d7a6e)" role="img" aria-label="Firefighter spraying water from a hose"></div>
      <div class="photo abs" style="left:28px;top:145px;background:linear-gradient(180deg,#f2f2f2,#c6c0c0)" role="img" aria-label="Row of red fire extinguishers"></div>
    </div>
    <div class="divider abs"></div>
    <div class="feature abs" style="left:277px;top:24px">
      <h2>Call for Fire Tender</h2>
      <div class="photo abs" style="left:40px;top:30px;background:linear-gradient(135deg,#8f8e88,#4c5058)" role="img" aria-label="Fire service officer at a dispatch console"></div>
      <div class="photo abs" style="left:40px;top:146px;background:linear-gradient(135deg,#9aa0a4,#b8292b)" role="img" aria-label="Red fire truck with yellow checked markings"></div>
    </div>
    <div class="more abs" style="left:195px;top:287px">More</div>
    <div class="more abs" style="left:463px;top:287px">More</div>
  </section>

  <aside class="hotline card abs">
    <h3>Call for Fire Information<br>24 hours a day</h3>
    <p>000 000 0000</p>
  </aside>

  <aside class="contact card abs">
    <h3>Contact Us</h3>
    <div>Mail: P.O Box 4120,<br>Marrowby, NSW 2260<br><br>Email: dana@krws.com.au<br>Mobile 0491570156<br>Accounts: accounts@kestrelmail.net.au</div>
  </aside>

  <section class="about card abs">
    <p>At kestrel ridge we believe that no matter how large or small your business is we can help you with the design, installation and the maintenance of your system to the standard which it was designed to.</p>
    <p>Kestrel Ridge is a fire protection company situated on the Central Coast of NSW and is currently servicing the Sydney, Central Coast and Hunter areas, We are always looking for new clients who are not happy with there current service providers and are looking for a Competitive priced alternative. Kestrel Ridge will come to your site and assess your fire service assets and provide a full quotation on a 12 month service contract.</p>
    <p>Kestrel Ridge can also supply quotations for any alterations to your Sprinklers,Hydrants &amp; Hose reel systems along with your fire detection and emergency lighting.</p>
    <p>Kestrel ridge is a owner operated business, so our reputation is our guarantee to do the best job we possibily can.</p>
  </section>

  <footer class="footer card abs">Copyright@2011</footer>
</div>
</body>
</html>
```